Webpage layout and company logo combination

We are trying to renovate an existing site to make it sharper and sophisticated in appearance. This is the existing site: http://www.kestrelhomesnj.com/agents.html . The new presentation should be bright, sharp, sophisticated and should incorporate two additional menu tabs. The menu tabs will be revised as follows: Property Listings, Property Management, Advisory & Consulting, Local Info, R/E Tools, Our Team (please disregard Korean language characters, which will be installed after English version is completed, separately).

It Company

```html
<!DOCTYPE html>
<html lang="en">
<head>
<meta charset="utf-8">
<title>Kestrel Homes</title>
<link rel="stylesheet" href="https://fonts.googleapis.com/css2?family=Open+Sans:ital,wght@0,400;0,600;0,700;1,400;1,600;1,700;1,800&family=Roboto+Condensed:wght@400;700&display=swap">
<style>
:root{
  --maroon:#6b2c47;
  --maroon-dark:#55233a;
  --olive:#b5b88a;
  --olive-light:#c9cba2;
  --olive-dark:#8f9362;
  --brown:#3a2a1b;
  --brown-tab:#4a3825;
  --ink:#333;
  --muted:#777;
  --line:#dcdcdc;
  --band:#ebebeb;
  --white:#fff;
}
*{box-sizing:border-box;margin:0;padding:0}
html,body{width:926px;height:1200px;overflow:hidden;background:var(--white);font-family:"Open Sans",Arial,sans-serif;color:var(--ink)}
.page{position:relative;width:926px;height:1200px;overflow:hidden}
.abs{position:absolute}

/* header */
.brand{left:97px;top:0;width:296px;height:71px}
.brand svg{position:absolute;inset:0}
.brand-name{position:absolute;left:18px;top:22px;display:flex;align-items:center;gap:10px;font-family:"Open Sans",sans-serif;font-weight:700;font-size:24px;color:var(--maroon-dark)}
.brand-mark{width:22px;height:22px;background:var(--maroon-dark)}
.contact{right:98px;top:17px;text-align:right;font-style:italic;font-weight:600;color:var(--maroon-dark);font-size:13px;line-height:19px}
.contact .tel{font-size:14px}

/* nav */
.nav{left:0;top:72px;width:926px;height:38px;background:var(--brown);border-bottom:2px solid #c8c8c8}
.nav ul{position:absolute;left:97px;top:0;display:flex;list-style:none;height:38px}
.nav li{height:38px;line-height:38px;margin-right:1px;text-align:center;white-space:nowrap;font-family:"Roboto Condensed",sans-serif;font-size:14px;color:#d0c8b8;background:var(--brown-tab)}
.nav li.active{background:var(--olive);color:var(--maroon)}
.flag{position:absolute;left:772px;top:0;width:58px;height:38px;background:#5c4a36;display:flex;align-items:center;justify-content:center}

/* hero */
.hero{left:0;top:112px;width:926px;height:365px;background:linear-gradient(100deg,#dfe9f2 0%,#b9cde0 30%,#8a9a86 45%,#2a2a2c 62%,#1d1d1f 100%)}
.caption{left:97px;top:279px;width:344px}
.caption h1{height:39px;line-height:39px;padding-left:15px;background:rgba(30,30,30,.78);color:#fff;font-family:"Roboto Condensed",sans-serif;font-weight:400;font-size:17px;width:218px}
.caption p{background:rgba(40,40,40,.6);color:#eee;font-size:10px;line-height:16px;padding:10px 15px 13px}
.dots{left:418px;top:451px;width:90px;height:26px;background:#fff;clip-path:polygon(0 0,100% 0,92% 100%,8% 100%);display:flex;gap:3px;justify-content:center;padding-top:6px}
.dots span{width:11px;height:11px;border-radius:50%;background:#999}
.dots span:first-child{background:#4a6aa0}

/* listings */
.tabs{left:97px;top:500px;display:flex;height:25px}
.tabs li{list-style:none;padding:0 14px;line-height:25px;font-size:12.5px;color:var(--maroon-dark);font-weight:400}
.tabs li.active{background:var(--maroon);color:#fff;font-weight:600}
.listing-panel{left:97px;top:525px;width:545px;height:396px;border:1px solid var(--line)}
.card{position:absolute;width:163px;height:163px;border:1px solid var(--line);background:#fff}
.card .photo{position:absolute;left:7px;top:7px;width:147px;height:88px}
.tag-sale{position:absolute;right:8px;top:7px;background:var(--maroon);color:#fff;font-size:9.5px;padding:2px 7px}
.price{position:absolute;left:7px;top:77px;background:var(--olive);color:#222;font-size:9.5px;font-weight:600;padding:2px 5px}
.card h3{position:absolute;left:11px;top:98px;font-size:11px;font-weight:400;color:var(--maroon)}
.card hr{position:absolute;left:7px;top:116px;width:147px;border:0;border-top:1px solid var(--line)}
.specs{position:absolute;left:11px;top:122px;width:145px;display:flex;font-size:9.5px;color:var(--maroon-dark)}
.specs div:nth-child(1){width:57px}
.specs div:nth-child(2){width:48px}
.specs svg{display:block;float:left;margin:7px 4px 0 0}
.specs b{display:block;font-weight:400}
.specs span{display:block;margin-top:7px;color:var(--muted);font-size:9.5px}
.zoom{position:absolute;left:60px;top:30px;width:28px;height:28px;border-radius:50%;background:#444;display:flex;align-items:center;justify-content:center}

/* agents */
.agents-title{left:663px;top:496px;width:167px;font-family:"Roboto Condensed",sans-serif;font-weight:400;font-size:16px;color:var(--maroon-dark);border-bottom:1px solid var(--line);padding-bottom:3px;display:flex;align-items:center;gap:5px}
.agent{position:absolute;left:661px;width:169px;height:62px;border:1px solid var(--line);background:#fff;overflow:hidden}
.agent .avatar{position:absolute;left:8px;top:8px;width:46px;height:46px;border-radius:50%;border:2px solid #ddd}
.agent .name{position:absolute;left:62px;top:5px;font-style:italic;font-size:11.5px;color:var(--maroon)}
.agent .info{position:absolute;left:62px;top:26px;width:104px;border-top:1px solid var(--line);padding-top:2px;font-style:italic;font-size:9.5px;line-height:15px;color:#444;white-space:nowrap}

/* action bar */
.band{left:0;top:968px;width:926px;height:195px;background:var(--band)}
.actions{left:97px;top:940px;width:733px;height:56px;display:flex}
.action{flex:1;display:flex;align-items:center;gap:10px;padding-left:12px;color:#fff;font-size:11.5px;line-height:15px;font-weight:600}
.action:nth-child(1){background:#222}
.action:nth-child(2){background:#333}
.action:nth-child(3){background:#444}
.action:nth-child(4){background:#555}
.action em{font-weight:800;font-size:17px}
.action .big{font-style:italic;font-weight:700;font-size:16px}

/* bottom */
.section-title{font-family:"Roboto Condensed",sans-serif;font-weight:400;font-size:15px;color:var(--maroon-dark);padding-bottom:6px;background:repeating-linear-gradient(90deg,#bbb 0 1px,transparent 1px 3px) bottom/100% 1px no-repeat}
.news{left:97px;top:1014px;width:156px}
.news-item{display:flex;gap:10px;margin-top:14px;font-size:10px;line-height:12.5px;color:#555;padding-bottom:8px;border-bottom:1px solid #d4d4d4}
.news-item .thumb{width:38px;height:36px;flex:none}
.news-item b{font-style:italic;font-weight:600;color:#222;font-size:10.5px}
.testimonial{left:277px;top:1018px;width:366px;height:106px;background:#fff;border:1px solid #ccc}
.testimonial .photo{position:absolute;left:7px;top:7px;width:110px;height:91px}
.testimonial h4{position:absolute;left:129px;top:14px;font-style:italic;font-weight:600;font-size:12px;color:var(--maroon)}
.testimonial .quote{position:absolute;left:129px;top:36px;font-size:22px;font-weight:700;color:#c6c6c6;line-height:22px;font-family:Georgia,serif}
.testimonial p{position:absolute;left:129px;top:40px;width:232px;font-size:9.5px;line-height:17px;color:#999;text-indent:16px}
.more{left:563px;top:1136px;font-style:italic;font-weight:600;font-size:9.5px;color:#222}
.company{left:671px;top:1014px;width:159px}
.company ul{list-style:none;margin-top:10px}
.company li{display:flex;gap:7px;font-style:italic;font-size:9.5px;line-height:13px;color:#333;margin-bottom:9px}
.company li svg{flex:none}
.social{left:667px;top:1128px;display:flex;gap:8px}
.social span{width:23px;height:23px;border-radius:50%;border:2px solid #999}
.social span.on{background:var(--maroon);border-color:var(--maroon)}

.footer{left:0;top:1163px;width:926px;height:37px;background:var(--olive)}
.crumbs{position:absolute;left:97px;top:12px;font-size:9.5px;color:#333;white-space:nowrap}
.crumbs a{color:#333;text-decoration:none}
.crumbs a:first-child{color:var(--maroon)}
.crumbs i{font-style:normal;margin:0 4px}
.copyright{position:absolute;right:97px;top:12px;font-size:9.5px;color:#333}
</style>
</head>
<body>
<svg width="0" height="0" style="position:absolute">
  <defs>
    <symbol id="i-garage" viewBox="0 0 16 12"><path d="M1 5 8 1l7 4v6H1z" fill="none" stroke="#999" stroke-width="1.2"/><path d="M4 7h8M4 9h8" stroke="#999"/></symbol>
    <symbol id="i-bed" viewBox="0 0 16 12"><path d="M1 2v9M1 8h14v3M4 6h10v2" fill="none" stroke="#999" stroke-width="1.2"/><circle cx="3" cy="5" r="1.4" fill="#999"/></symbol>
    <symbol id="i-bath" viewBox="0 0 16 12"><path d="M2 6h13v2a3 3 0 0 1-3 3H5a3 3 0 0 1-3-3zM3 6V2h3" fill="none" stroke="#999" stroke-width="1.2"/></symbol>
  </defs>
</svg>

<div class="page">
  <header>
    <div class="brand abs">
      <svg width="296" height="71" viewBox="0 0 296 71"><defs><linearGradient id="tab" x1="0" y1="0" x2="0" y2="1"><stop offset="0" stop-color="#d6d8b0"/><stop offset="1" stop-color="#aeb27c"/></linearGradient></defs><path d="M0 0h242l52 71H0z" fill="url(#tab)" stroke="#8f9362"/></svg>
      <div class="brand-name"><span class="brand-mark"></span>Kestrel Homes</div>
    </div>
    <address class="contact abs">Add: 418 Linden Crest Ave , NJ 07399<br><span class="tel">Tel: (800)555-0142&nbsp; Fax: (201)555-0177</span></address>
  </header>

  <nav class="nav abs">
    <ul>
      <li class="active" style="width:52px">Home</li>
      <li style="width:112px">Property Listings</li>
      <li style="width:142px">Property Management</li>
      <li style="width:138px">Advisory &amp; Consulting</li>
      <li style="width:75px">Local Info</li>
      <li style="width:71px">R/E Tools</li>
      <li style="width:77px">Our Team</li>
    </ul>
    <div class="flag"><svg width="34" height="22" viewBox="0 0 60 36"><rect width="60" height="36" fill="#1f3b80"/><path d="M0 0l60 36M60 0 0 36" stroke="#fff" stroke-width="7"/><path d="M0 0l60 36M60 0 0 36" stroke="#c8102e" stroke-width="2.5"/><path d="M30 0v36M0 18h60" stroke="#fff" stroke-width="11"/><path d="M30 0v36M0 18h60" stroke="#c8102e" stroke-width="6"/></svg></div>
  </nav>

  <section class="hero abs" role="img" aria-label="Photo of a hand in a suit sleeve holding a model house on a patch of lawn under a blue sky"></section>
  <div class="caption abs">
    <h1>Welcome to Kestrel Homes</h1>
    <p>Kestrel Homes is your online resource of buying, selling and finacing for your recidential or commercial real estate. We will assist your real estate needs uor integrity and helpful experience.</p>
  </div>
  <div class="dots abs"><span></span><span></span><span></span><span></span><span></span></div>

  <ul class="tabs abs">
    <li class="active">Family House</li><li>Land</li><li>Apartment</li><li>Cottage</li>
  </ul>
  <section class="listing-panel abs">
    <article class="card" style="left:13px;top:12px">
      <div class="photo" role="img" aria-label="Bright empty townhouse interior" style="background:linear-gradient(135deg,#e9e9e9,#cfcfcf)"></div>
      <div class="zoom"><svg width="14" height="14" viewBox="0 0 14 14"><circle cx="6" cy="6" r="4.2" fill="none" stroke="#fff" stroke-width="1.6"/><path d="M9 9l4 4M4 6h4M6 4v4" stroke="#fff" stroke-width="1.6"/></svg></div>
      <span class="tag-sale">For sale</span><span class="price">$625,000</span>
      <h3>Townhouse</h3><hr>
      <div class="specs"><div><b>Garage</b><svg width="16" height="12"><use href="#i-garage"/></svg><span>1</span></div><div><b>Beds</b><svg width="16" height="12"><use href="#i-bed"/></svg><span>2</span></div><div><b>Baths</b><svg width="16" height="12"><use href="#i-bath"/></svg><span>2</span></div></div>
    </article>
    <article class="card" style="left:190px;top:12px">
      <div class="photo" role="img" aria-label="Brick townhouses behind a green lawn" style="background:linear-gradient(180deg,#d3dde6 0,#8c8f7a 45%,#4f6d3a 100%)"></div>
      <span class="tag-sale">For sale</span><span class="price">$625,000</span>
      <h3>Townhouse</h3><hr>
      <div class="specs"><div><b>Garage</b><svg width="16" height="12"><use href="#i-garage"/></svg><span>1</span></div><div><b>Beds</b><svg width="16" height="12"><use href="#i-bed"/></svg><span>2</span></div><div><b>Baths</b><svg width="16" height="12"><use href="#i-bath"/></svg><span>2</span></div></div>
    </article>
    <article class="card" style="left:367px;top:12px">
      <div class="photo" role="img" aria-label="Atrium lobby with plants seen from above" style="background:linear-gradient(135deg,#6e5a40,#a88c64 50%,#4c5b35)"></div>
      <span class="tag-sale">For sale</span><span class="price">$625,000</span>
      <h3>Townhouse</h3><hr>
      <div class="specs"><div><b>Garage</b><svg width="16" height="12"><use href="#i-garage"/></svg><span>1</span></div><div><b>Beds</b><svg width="16" height="12"><use href="#i-bed"/></svg><span>2</span></div><div><b>Baths</b><svg width="16" height="12"><use href="#i-bath"/></svg><span>2</span></div></div>
    </article>
    <article class="card" style="left:13px;top:189px">
      <div class="photo" role="img" aria-label="White multi-storey house on a street with parked cars" style="background:linear-gradient(180deg,#bcd3ea 0,#e6e6e6 40%,#7d6a5a 100%)"></div>
      <span class="tag-sale">For sale</span><span class="price">$625,000</span>
      <h3>Townhouse</h3><hr>
      <div class="specs"><div><b>Garage</b><svg width="16" height="12"><use href="#i-garage"/></svg><span>1</span></div><div><b>Beds</b><svg width="16" height="12"><use href="#i-bed"/></svg><span>2</span></div><div><b>Baths</b><svg width="16" height="12"><use href="#i-bath"/></svg><span>2</span></div></div>
    </article>
    <article class="card" style="left:190px;top:189px">
      <div class="photo" role="img" aria-label="Suburban street with autumn trees and houses" style="background:linear-gradient(180deg,#d9dde2 0,#a97a55 50%,#8b8b8b 100%)"></div>
      <span class="tag-sale">For sale</span><span class="price">$625,000</span>
      <h3>Townhouse</h3><hr>
      <div class="specs"><div><b>Garage</b><svg width="16" height="12"><use href="#i-garage"/></svg><span>1</span></div><div><b>Beds</b><svg width="16" height="12"><use href="#i-bed"/></svg><span>2</span></div><div><b>Baths</b><svg width="16" height="12"><use href="#i-bath"/></svg><span>2</span></div></div>
    </article>
    <article class="card" style="left:367px;top:189px">
      <div class="photo" role="img" aria-label="Modern living room with kitchen counter and stools" style="background:linear-gradient(135deg,#e2dcd2,#8b7b68 60%,#3c3530)"></div>
      <span class="tag-sale">For sale</span><span class="price">$625,000</span>
      <h3>Townhouse</h3><hr>
      <div class="specs"><div><b>Garage</b><svg width="16" height="12"><use href="#i-garage"/></svg><span>1</span></div><div><b>Beds</b><svg width="16" height="12"><use href="#i-bed"/></svg><span>2</span></div><div><b>Baths</b><svg width="16" height="12"><use href="#i-bath"/></svg><span>2</span></div></div>
    </article>
  </section>

  <h2 class="agents-title abs"><svg width="24" height="14" viewBox="0 0 24 14"><circle cx="6" cy="4" r="3" fill="#6b2c47"/><circle cx="18" cy="4" r="3" fill="#6b2c47"/><circle cx="12" cy="5" r="3.4" fill="#6b2c47"/><path d="M0 14a6 5 0 0 1 12 0zM12 14a6 5 0 0 1 12 0zM5 14a7 6 0 0 1 14 0z" fill="#6b2c47"/></svg>Our Agents</h2>
  <aside>
    <div class="agent" style="top:526px"><div class="avatar" role="img" aria-label="Agent portrait" style="background:#a7a0a0"></div><div class="name">Harold Marlow</div><div class="info">Cell: 201-555-0110<br>hmarlow@khnj.com</div></div>
    <div class="agent" style="top:592px"><div class="avatar" role="img" aria-label="Agent portrait" style="background:#8fae7c"></div><div class="name">Jay Reno</div><div class="info">Cell: (917)555-0123<br>jreno@khnj.com</div></div>
    <div class="agent" style="top:658px"><div class="avatar" role="img" aria-label="Agent portrait" style="background:#6f8fb3"></div><div class="name">Sofia Lund</div><div class="info">Cell: (201)555-0134<br>slund@khnj.com</div></div>
    <div class="agent" style="top:724px"><div class="avatar" role="img" aria-label="Agent portrait" style="background:#7c8fa6"></div><div class="name">Kevin Hale</div><div class="info">Cell: (201)555-0145<br>khale@khnj.com</div></div>
    <div class="agent" style="top:790px"><div class="avatar" role="img" aria-label="Agent portrait" style="background:#b49a86"></div><div class="name">Jason Vey</div><div class="info">Cell: (201)555-0156<br>jvey@khnj.com</div></div>
    <div class="agent" style="top:856px"><div class="avatar" role="img" aria-label="Agent portrait" style="background:#c9b8a8"></div><div class="name">Scott Rowan</div><div class="info">Cell: (201)555-0167<br>srowan@khnj.com</div></div>
  </aside>

  <div class="band abs"></div>
  <section class="actions abs">
    <div class="action"><svg width="22" height="24" viewBox="0 0 22 24"><path d="M2 9 11 1l9 8v13H2z" fill="#fff" transform="rotate(-25 11 12)"/><circle cx="11" cy="8" r="2" fill="#222"/></svg><div>CLICK HERE FOR <em>FREE</em><br>APPRAISAL</div></div>
    <div class="action"><svg width="28" height="22" viewBox="0 0 28 22"><path d="M2 6c0-3 24-3 24 0v3h-6V6H8v3H2z" fill="#fff"/><rect x="5" y="10" width="18" height="11" rx="2" fill="#fff"/><circle cx="14" cy="15.5" r="3" fill="#333"/></svg><div>CALL US<br><span class="big">(800)555-0142</span></div></div>
    <div class="action"><svg width="20" height="26" viewBox="0 0 20 26"><rect x="1" y="3" width="18" height="22" rx="1" fill="#fff"/><rect x="6" y="0" width="8" height="5" fill="#fff"/><path d="M5 10h10M5 14h10M5 18h10" stroke="#444" stroke-width="1.5"/></svg><div>ONLINE <span class="big">PROPERTY</span><br>MAGAZINE</div></div>
    <div class="action"><svg width="34" height="26" viewBox="0 0 34 26"><rect x="1" y="1" width="20" height="24" rx="2" fill="#fff"/><rect x="4" y="4" width="14" height="5" fill="#555"/><path d="M5 13h3M9 13h3M14 13h3M5 17h3M9 17h3M14 17h3M5 21h3M9 21h3M14 21h3" stroke="#555" stroke-width="2"/><text x="23" y="19" font-size="16" font-weight="700" fill="#fff" font-family="Open Sans,sans-serif">$</text></svg><div>MORTGAGE<br><span class="big">CALCULATOR</span></div></div>
  </section>

  <section class="news abs">
    <h2 class="section-title">News</h2>
    <div class="news-item"><div class="thumb" role="img" aria-label="News thumbnail" style="background:#d49a4a"></div><div><b>Monday 03 Mar 2014</b><br>Conference Overview<br>We hope to see the....</div></div>
    <div class="news-item" style="border:0"><div class="thumb" role="img" aria-label="News thumbnail" style="background:#b99a94"></div><div><b>Monday 03 Mar 2014</b><br>Conference Overview<br>We hope to see the....</div></div>
  </section>

  <section class="testimonial abs">
    <div class="photo" role="img" aria-label="Client portrait" style="background:linear-gradient(135deg,#5a6e8a,#b9a79a)"></div>
    <h4>Client Name</h4>
    <span class="quote">“</span>
    <p>Lorem ipsum dolor sit amet, ctetur adipiscing elit. Nullam volutpat egestas neque, non hendrerit ipsum fringilla quis. Donec ut neque mauris.</p>
  </section>
  <a class="more abs">More Testimonials</a>

  <section class="company abs">
    <h2 class="section-title">Kestrel Homes</h2>
    <ul>
      <li><svg width="16" height="16" viewBox="0 0 16 16"><path d="M8 1a5 5 0 0 1 5 5c0 4-5 9-5 9S3 10 3 6a5 5 0 0 1 5-5z" fill="none" stroke="#6b2c47" stroke-width="1.4"/><path d="M6 6h4M8 4v4" stroke="#6b2c47" stroke-width="1.4"/></svg><span>418 Linden Crest Ave , NJ 07399</span></li>
      <li><svg width="16" height="14" viewBox="0 0 16 14"><path d="M3 1l3 3-2 2c1 2 2 3 4 4l2-2 3 3-2 2C6 13 1 8 1 3z" fill="#6b2c47"/></svg><span>(800)555-0142</span></li>
      <li><svg width="16" height="12" viewBox="0 0 16 12"><rect x="1" y="1" width="14" height="10" fill="#6b2c47"/><path d="M1 1l7 6 7-6" fill="none" stroke="#fff"/></svg><span>hmarlow@khnj.com</span></li>
    </ul>
  </section>
  <div class="social abs"><span class="on"></span><span></span><span></span><span></span><span></span></div>

  <footer class="footer abs">
    <div class="crumbs"><a>Home</a><i>/</i><a>Property Listings</a><i>/</i><a>Property Management</a><i>/</i><a>Advisory &amp; Consulting</a><i>/</i><a>Local Info</a><i>/</i><a>R/E Tools</a><i>/</i><a>Our Team</a></div>
    <div class="copyright">Kestrel Homes © 2014. All Rights Reserved.</div>
  </footer>
</div>
</body>
</html>
```